contemporary upscale hair salon

we need a business card design for a modern upscale salon. I would like the card to be vertical, simple, and easy to read. I would like a black matte finish on the info side with white on the back of the card, white lettering with a splash of red incorporated somewhere in there. I also want to incorporate embossing and/or cut out in the letters. The info I would like; Name of the business (Velora Salon) stylist name (Janet) phone number(4075319264) and web address (www.veloraexample.com) I am open to putting shears on the card but without it looking too cheap. Looking for something really modern and edgy. these are just ideas I have, but feel free to show me your creative ideas.
please note: the website is still under construction please do not use any images or colors off the web page. Also i currently do not have a logo, that will be a future project.

```html
<!DOCTYPE html>
<html lang="en">
<head>
<meta charset="utf-8">
<title>Velora Salon – Business Card</title>
<link rel="stylesheet" href="https://fonts.googleapis.com/css2?family=Open+Sans:wght@400;600&display=swap">
<style>
  :root {
    --stage: #e6e6e6;
    --card-white: #f1f1f0;
    --card-black: #232323;
    --magenta: #d13a94;
    --rule: #3a3a3a;
    --text-light: #ffffff;
  }
  * { box-sizing: border-box; margin: 0; padding: 0; }
  html, body {
    width: 1000px;
    height: 1200px;
    overflow: hidden;
    background: var(--stage);
    font-family: "Open Sans", Arial, sans-serif;
  }
  .canvas {
    position: relative;
    width: 1000px;
    height: 1200px;
  }
  .card {
    position: absolute;
    top: 250px;
    width: 400px;
    height: 700px;
    box-shadow: 0 6px 18px rgba(0,0,0,0.18);
  }
  .card--back {
    left: 66px;
    background: var(--card-white);
  }
  .card--info {
    left: 534px;
    background: var(--card-black);
  }
  .brand-name {
    position: absolute;
    left: 0;
    right: 0;
    text-align: center;
    color: var(--magenta);
    font-weight: 400;
    letter-spacing: 1px;
    text-transform: uppercase;
    white-space: nowrap;
  }
  .card--back .brand-name {
    top: 322px;
    font-size: 36px;
  }
  .card--info .brand-name {
    top: 300px;
    font-size: 34px;
  }
  .stylist-band {
    position: absolute;
    top: 70px;
    left: 90px;
    width: 250px;
    height: 58px;
    background: var(--magenta);
    color: var(--text-light);
    font-size: 19px;
    font-weight: 400;
    letter-spacing: 0.5px;
    text-transform: uppercase;
    display: flex;
    align-items: center;
    justify-content: center;
    white-space: nowrap;
  }
  .contact-box {
    position: absolute;
    left: 30px;
    right: 30px;
    bottom: 92px;
    height: 210px;
    border: 1px solid var(--rule);
    display: flex;
  }
  .contact-cell {
    flex: 1;
    position: relative;
  }
  .contact-cell + .contact-cell {
    border-left: 1px solid var(--rule);
  }
  .contact-text {
    position: absolute;
    left: 50%;
    top: 50%;
    transform: translate(-50%, -50%) rotate(-90deg);
    color: var(--magenta);
    font-size: 13px;
    font-weight: 600;
    letter-spacing: 1px;
    white-space: nowrap;
  }
  .contact-text--web { font-style: italic; }
  .accent-bar {
    position: absolute;
    left: 30px;
    right: 30px;
    bottom: 40px;
    height: 52px;
    background: var(--magenta);
  }
</style>
</head>
<body>
  <main class="canvas">
    <section class="card card--back" aria-label="Card back">
      <p class="brand-name">Velora Salon</p>
    </section>

    <section class="card card--info" aria-label="Card front with stylist details">
      <div class="stylist-band">Stylist Name: Janet</div>
      <p class="brand-name">Velora Salon</p>
      <div class="contact-box">
        <div class="contact-cell">
          <span class="contact-text contact-text--phone">4075319264</span>
        </div>
        <div class="contact-cell">
          <span class="contact-text contact-text--web">www.veloraexample.com</span>
        </div>
      </div>
      <div class="accent-bar"></div>
    </section>
  </main>
</body>
</html>
```